Tidewell Estates Agency Guarantee

We need a flyer to promote a Sydney based property management agency.
We specialise in Property Management on the Northern Beaches of Sydney. A small boutique agency that prides itself on high quality customer service and the lowest fees.
We would like this flyer to promote our listed features in the document provided and focus on our money back guarantee.
The flyer must:
- be designed to match our website www.tidewellestatesagency.com.au
- Contain our logo and contact details
- Use the attached photoshop template for bleed, sizing and fold lines
- final files must include a print ready PDF and fully editable PSD (photoshop) file with included fonts.
Attached are the following files:
Contact details are:
Name: Tom Hadley
Tel: 0498 316 207
email: tom@tidewellestatesagency.com.au
Office: Level 3, 17 Carrow Rd, Merrigal NSW 2109
Web: www.tidewellestatesagency.com.au
Target Market(s)
35-75yo Male and Females that own investment properties on Sydney's Norther Beaches
Industry/Entity Type
Real Estate
Requirements
Must have
- The flyer must:
- - Be double sided and colour
- - be designed to match our website www.tidewellestatesagency.com.au
- - Contain our logo and contact details
- - Use the attached photoshop template for bleed, sizing and fold lines
- - final files must include a print ready PDF and fully editable PSD (photoshop) file with included fonts.
Nice to have
- A Money back guarantee "stamp"

```html
<!DOCTYPE html>
<html lang="en">
<head>
<meta charset="utf-8">
<title>Tidewell Estates Agency – Trifold Brochure</title>
<link rel="stylesheet" href="https://fonts.googleapis.com/css2?family=Oswald:wght@500;700&family=Open+Sans:wght@400;600;700&display=swap">
<style>
:root{
  --canvas:#d8d9da;
  --teal:#2a9ca1;
  --teal-dark:#1d7c81;
  --teal-light:#58c3c7;
  --ink:#1b1b1b;
  --body:#4a4f53;
  --paper:#f7f9fa;
  --paper-shade:#e7ecee;
  --white:#ffffff;
}
*{box-sizing:border-box;margin:0;padding:0}
html,body{width:1200px;height:1200px;overflow:hidden;background:var(--canvas)}
body{font-family:"Open Sans",Arial,sans-serif;color:var(--body);position:relative}
.spread{position:absolute;left:40px;width:1120px;height:520px;display:grid;grid-template-columns:repeat(3,1fr);box-shadow:0 10px 28px rgba(0,0,0,.18);background:var(--paper)}
.spread--outside{top:50px}
.spread--inside{top:630px}
.panel{position:relative;overflow:hidden;background:linear-gradient(180deg,var(--white),var(--paper) 60%,var(--paper-shade));padding:22px 22px 0}
.panel + .panel{border-left:1px solid rgba(0,0,0,.06)}
.footer-band{position:absolute;left:0;right:0;bottom:0;height:26px;background:var(--teal);color:var(--white);font-size:9.5px;letter-spacing:.3px;display:flex;align-items:center;padding-left:22px;z-index:3}
.section-title{font-family:"Oswald",Arial,sans-serif;font-weight:700;color:var(--teal);font-size:11px;letter-spacing:.4px;text-transform:uppercase;margin:10px 0 4px}
.section-title--bar{display:inline-block;background:var(--teal);color:var(--white);padding:2px 8px;margin-top:0}
.copy{font-size:8.6px;line-height:1.5;text-align:justify}
.bullet{font-size:8.6px;line-height:1.5;padding-left:10px;position:relative}
.bullet::before{content:"";position:absolute;left:1px;top:5px;width:4px;height:4px;border-radius:50%;background:var(--teal)}
.photo{position:absolute;z-index:1}
.photo--harbour{background:linear-gradient(135deg,#7fb8d8,#2f6f96 55%,#1d3f57)}
.photo--street{background:linear-gradient(135deg,#9ccde3,#3d6f88 50%,#26404e)}
.photo--house{background:linear-gradient(160deg,#a9d2ec,#6c7f86 45%,#4a6a3a)}
.photo--coast{background:linear-gradient(160deg,#b9dcef,#4f93b8 45%,#2a6a8a 75%,#7a8f86)}
.photo--sign{background:linear-gradient(135deg,#5fa6cf,#1d4663)}
.accent{position:absolute;z-index:2;pointer-events:none}
.ring{fill:var(--teal-light);stroke:var(--teal-dark);stroke-width:3}
.top-photos{display:grid;grid-template-columns:1.3fr 1fr;gap:8px;height:92px;margin:0 -22px 4px 0}
.top-photos .photo{position:relative}
.portrait{width:78px;height:78px;border-radius:50%;border:4px solid var(--teal);background:linear-gradient(135deg,#c9d6dc,#7d949e);position:absolute;left:30px;top:300px;z-index:2}
.contact{position:absolute;left:124px;top:296px;right:18px;z-index:2}
.contact .name{font-family:"Oswald",Arial,sans-serif;font-weight:700;font-size:12px;color:var(--teal);text-transform:uppercase}
.contact .role{font-size:8.5px;margin-bottom:6px}
.contact-row{display:flex;gap:6px;align-items:flex-start;font-size:8.6px;line-height:1.35;margin-bottom:5px}
.contact-row svg{flex:0 0 11px;width:11px;height:11px;fill:var(--teal);margin-top:1px}
.brand{position:absolute;right:22px;top:24px;display:flex;align-items:center;gap:6px;font-family:"Open Sans",Arial,sans-serif;font-weight:700;font-size:11px;color:var(--ink);letter-spacing:.3px;text-transform:uppercase;z-index:3}
.brand-dot{width:10px;height:10px;border-radius:50%;background:var(--teal)}
.headline{position:absolute;left:26px;bottom:48px;z-index:3;font-family:"Oswald",Arial,sans-serif;font-weight:700;line-height:.92;text-transform:uppercase;transform:skewX(-8deg)}
.headline span{display:block}
.headline .l1{font-size:50px;color:var(--teal)}
.headline .l2{font-size:36px;color:var(--ink)}
.headline .l3{font-size:46px;color:var(--teal)}
.phone-line{position:absolute;left:40px;bottom:50px;display:flex;align-items:center;gap:10px;font-size:18px;color:var(--ink);z-index:3}
.phone-line svg{width:22px;height:22px;fill:var(--teal)}
.rule{position:absolute;left:22px;right:22px;bottom:90px;height:1px;background:var(--teal);opacity:.6}
</style>
</head>
<body>

<!-- Outside of the brochure -->
<section class="spread spread--outside" aria-label="Brochure outside">
  <div class="panel">
    <h3 class="section-title section-title--bar">Our guarantee:</h3>
    <p class="copy" style="margin-top:6px">We stand behind every tenancy we manage. If you are not satisfied with our service within the first three months, we will refund your management fees in full, with no hidden conditions or fine print.</p>
    <h3 class="section-title">Keeping it simple:</h3>
    <p class="copy">One flat fee covers everything. No leasing charges, no advertising costs and no surprise invoices at the end of the financial year.</p>
    <h3 class="section-title">Senior property manager:</h3>
    <p class="copy">Your property is looked after by one experienced manager from start to finish, so you always know who to call and who is accountable.</p>
    <div class="photo photo--street" role="img" aria-label="Photo of a sunny harbourside street with trees and water" style="left:0;right:0;bottom:26px;height:200px;clip-path:polygon(0 0,100% 62%,100% 100%,0 100%)"></div>
    <svg class="accent" style="left:0;bottom:26px" width="374" height="200" viewBox="0 0 374 200"><polygon points="0,0 374,124 374,140 0,14" fill="var(--teal)" opacity=".85"/></svg>
    <div class="footer-band">www.tidewellestatesagency.com.au</div>
  </div>

  <div class="panel">
    <div class="top-photos">
      <div class="photo photo--sign" role="img" aria-label="Photo of a beachside street sign against blue sky"></div>
      <div class="photo photo--house" role="img" aria-label="Photo of a modern home with garden"></div>
    </div>
    <h3 class="section-title">What separates Tidewell Estates Agency:</h3>
    <p class="copy">We are a small boutique agency on the Northern Beaches. We keep our portfolio deliberately small so every owner receives personal attention and the lowest fees in the area.</p>
    <svg class="accent" style="left:0;top:250px" width="374" height="270" viewBox="0 0 374 270"><polygon points="0,80 374,0 374,14 0,94" fill="var(--teal)" opacity=".25"/><polygon points="0,270 150,90 166,90 18,270" fill="var(--teal)" opacity=".2"/></svg>
    <div class="portrait" role="img" aria-label="Portrait photo of the senior property manager"></div>
    <div class="contact">
      <h3 class="section-title" style="margin-top:0">Contact details</h3>
      <div class="name">Tom Hadley</div>
      <div class="role">Senior Property Manager</div>
      <div class="contact-row"><svg viewBox="0 0 12 12"><path d="M6 0a4 4 0 0 0-4 4c0 3 4 8 4 8s4-5 4-8a4 4 0 0 0-4-4zm0 5.6A1.6 1.6 0 1 1 6 2.4a1.6 1.6 0 0 1 0 3.2z"/></svg><span>Level 3, 17 Carrow Rd,<br>Merrigal NSW 2109</span></div>
      <div class="contact-row"><svg viewBox="0 0 12 12"><path d="M2.4 0 4.5 2.6 3.4 4.2a7 7 0 0 0 4.4 4.4l1.6-1.1L12 9.6 10.4 12C4.8 12 0 7.2 0 1.6z"/></svg><span>0498 316 207</span></div>
      <div class="contact-row"><svg viewBox="0 0 12 12"><path d="M0 2h12v8H0zm1 1v.4l5 3.3 5-3.3V3zm0 1.6V9h10V4.6L6 7.9z"/></svg><span>tom@tidewellestatesagency.com.au</span></div>
      <div class="contact-row"><svg viewBox="0 0 12 12"><path d="M6 0a6 6 0 1 0 0 12A6 6 0 0 0 6 0zm0 1c.8.8 1.4 2.2 1.6 4.5H4.4C4.6 3.2 5.2 1.8 6 1zM1 6.5h2.4c.1 1.8.5 3.2 1.1 4.3A5 5 0 0 1 1 6.5zm0-1A5 5 0 0 1 4.5 1.2c-.6 1.1-1 2.5-1.1 4.3zm5 5.5c-.8-.8-1.4-2.2-1.6-4.5h3.2C7.4 8.8 6.8 10.2 6 11zm1.5-.2c.6-1.1 1-2.5 1.1-4.3H11a5 5 0 0 1-3.5 4.3zM8.6 5.5c-.1-1.8-.5-3.2-1.1-4.3A5 5 0 0 1 11 5.5z"/></svg><span>www.tidewellestatesagency.com.au</span></div>
    </div>
    <div class="footer-band"></div>
  </div>

  <div class="panel">
    <div class="brand"><span class="brand-dot"></span>Tidewell Estates Agency</div>
    <div class="photo photo--house" role="img" aria-label="Photo of modern townhouses with landscaped gardens" style="left:0;right:0;top:60px;height:230px;clip-path:polygon(0 0,100% 0,100% 62%,58% 100%,0 38%)"></div>
    <svg class="accent" style="left:0;top:60px" width="374" height="250" viewBox="0 0 374 250"><polyline points="0,87 217,230 374,143" fill="none" stroke="var(--teal)" stroke-width="6"/><circle class="ring" cx="217" cy="234" r="11"/></svg>
    <h1 class="headline"><span class="l1">Property</span><span class="l2">Management</span><span class="l3">Done Right!</span></h1>
    <div class="footer-band">www.tidewellestatesagency.com.au</div>
  </div>
</section>

<!-- Inside of the brochure -->
<section class="spread spread--inside" aria-label="Brochure inside">
  <div class="panel">
    <h3 class="section-title" style="margin-top:0;font-size:13px;color:var(--ink)">Our guarantee:</h3>
    <h3 class="section-title">Strict screening process:</h3>
    <p class="copy">All tenants are checked against national databases, employment records and previous landlord references before any lease is offered.</p>
    <h3 class="section-title">Quality tenant database and corporate re-locations:</h3>
    <p class="copy">We maintain a list of pre-approved applicants and work with local employers relocating staff, so quality tenants are often ready before your property is even listed.</p>
    <h3 class="section-title">Quick to act and tenant a property:</h3>
    <p class="copy">Being a boutique agency means fast decisions. Most of our properties are leased within two weeks of going to market.</p>
    <div class="photo photo--harbour" role="img" aria-label="Photo of a marina with moored boats and waterfront homes" style="left:0;right:0;bottom:26px;height:230px;clip-path:polygon(0 0,22% 0,68% 100%,0 100%)"></div>
    <svg class="accent" style="left:0;bottom:26px" width="374" height="240" viewBox="0 0 374 240"><polyline points="0,10 84,10 254,240" fill="none" stroke="var(--teal)" stroke-width="6"/><circle class="ring" cx="84" cy="12" r="11"/></svg>
    <div class="footer-band">www.tidewellestatesagency.com.au</div>
  </div>

  <div class="panel">
    <h3 class="section-title" style="margin-top:40px">6 monthly property reports:</h3>
    <p class="copy">Twice a year you receive a detailed written report with photos, covering condition, rent review and any upcoming repairs.</p>
    <h3 class="section-title">Landlord portal:</h3>
    <p class="copy">Log in at any time to view statements, invoices, inspection reports and rent payments for every property you own.</p>
    <h3 class="section-title">Maintenance/ renovation plan:</h3>
    <p class="copy">We help you plan small improvements that protect your asset, lift the rent and keep good tenants staying longer.</p>
    <svg class="accent" style="left:0;top:0" width="374" height="520" viewBox="0 0 374 520"><polygon points="0,0 20,0 0,60" fill="var(--teal)" opacity=".3"/><polygon points="374,0 374,40 330,0" fill="var(--teal)" opacity=".3"/></svg>
    <div class="footer-band"></div>
  </div>

  <div class="panel">
    <div class="photo photo--coast" role="img" aria-label="Photo of a rocky coastline and ocean pool under blue sky" style="left:0;right:0;top:0;height:200px;clip-path:polygon(0 0,100% 0,100% 100%)"></div>
    <svg class="accent" style="left:0;top:0" width="374" height="210" viewBox="0 0 374 210"><line x1="0" y1="0" x2="362" y2="196" stroke="var(--teal)" stroke-width="6"/><circle class="ring" cx="360" cy="196" r="11"/></svg>
    <div style="position:relative;z-index:2;margin-top:150px;padding-right:40px">
      <p class="bullet">Building Equity: smart upgrades add value and rental return over time.</p>
      <p class="bullet">Ensuring small maintenance issues never become expensive problems later.</p>
      <h3 class="section-title">Retaining great tenants:</h3>
      <p class="copy">Happy tenants stay longer and care for your home. We reward reliable renters and keep communication friendly and prompt.</p>
      <h3 class="section-title">Our broad team:</h3>
      <p class="copy">We work with trusted local trades, mortgage brokers and accountants so you get the best advice for your investment.</p>
    </div>
    <div class="rule"></div>
    <div class="phone-line"><svg viewBox="0 0 12 12"><path d="M2.4 0 4.5 2.6 3.4 4.2a7 7 0 0 0 4.4 4.4l1.6-1.1L12 9.6 10.4 12C4.8 12 0 7.2 0 1.6z"/></svg>0498 316 207</div>
    <div class="footer-band"></div>
  </div>
</section>

</body>
</html>
```